Product sheet for managing talented people!

We need a new product sheet to describe our method of helping organisations to manage their talented people! We have selected a rowing team as the graphical theme (sample attached - please select or suggest a new picture if you want). We have also attached a powerpoint slide with our model (this is the service we offer).

FRONT PAGE

We are looking for an eye-catching front page that uses our 1. "Kestrel Growth Model"; 2. a picture of a rowing team of 8, and 3. our logo and 1800 KESTRL phone number (1800 537 875).

Step 1 - Assess key positions to determine your Talent Management Priorities.

Step 2 - Organisational psychology support helps individuals self-evaluate (see page 2 for details).

Step 3 - Facilitate agreement with manager and embed best-practice in organisational fairness.

Step 4 - Tailor career development and redeployment options based on shared understanding.

Step 5 - Evaluate ROI for individual performance and engagement.

BACK PAGE

The second page will have more detail of each of the talent categories also included in the powerpoint slide. Logo attached also. Please also view our website as the graphics should give you a sense of the look and feel of our brand - www.kestrelgm.com.au We have also added another flyer that we still use - please do not reverse the logo on this project - use in current form. CORPORATE LOGO / COLOUR GUIDE
C100 M50 Y0 K0
C100 M50 Y0 K0
C100 M50 Y0 K0
Gradient
C100 M60 Y0 K40
C100 M45 Y0 K0
C100 M20 Y0 K0
C70 M0 Y0 K0
PMS 2935 C
PMS 2935 C 75% Tint
PMS 2935 C
PMS Process Cyan C

The successful flyer will need to be print ready (as per attached example) and in pdf form so that we can print and/or send as a PDF.

Thanks.

Target Market(s)

Human Resource Managers in business and government.

Industry/Entity Type

Product

Requirements
Must have
• Eye-catching graphics with a rowing team theme. Colours consistent with our corporate colour codes.
Nice to have
• Please add small "trademark" symbol to the logo. This is small TM in a circle and usually placed at top right hand of logo. PLease add our website address www.kestrelgm.com
Should not have
• Please do not "reverse" the logo - use as is.

```html
<!DOCTYPE html>
<html lang="en">
<head>
<meta charset="utf-8">
<title>Kestrel Growth Model – Product Sheet</title>
<link rel="stylesheet" href="https://fonts.googleapis.com/css2?family=Open+Sans:ital,wght@0,300;0,400;0,600;0,700;1,300&display=swap">
<style>
  :root {
    --backdrop: #c9c9c9;
    --paper: #ffffff;
    --tint-1: #6ccdf1;
    --tint-2: #17bcee;
    --tint-3: #1a9bd7;
    --tint-4: #0e70b6;
    --navy: #0b3e74;
    --mid-blue: #1a8ed5;
    --cyan: #16bff0;
    --ink-blue: #1f6fb2;
    --brand-blue: #3f5fb0;
    --headline-blue: #1a8fd0;
    --photo-light: #a9c7e2;
    --photo-dark: #3e6f9c;
  }
  * { box-sizing: border-box; margin: 0; padding: 0; }
  html, body { width: 1200px; height: 900px; overflow: hidden; }
  body {
    background: var(--backdrop);
    font-family: "Open Sans", sans-serif;
    font-weight: 300;
    position: relative;
  }
  .page {
    position: absolute;
    top: 62px;
    width: 564px;
    height: 796px;
    background: var(--paper);
  }
  .page--front { left: 37px; }
  .page--back { left: 618px; }

  .hero-photo {
    position: absolute; left: 15px; top: 15px; width: 534px; height: 219px;
    background: linear-gradient(120deg, var(--photo-dark) 0%, var(--photo-light) 45%, #dfe9f3 70%, var(--photo-dark) 100%);
  }
  .headline {
    position: absolute; left: 15px; top: 250px; width: 534px;
    text-align: center; font-size: 20.5px; color: var(--headline-blue);
    letter-spacing: 0.2px;
  }
  .headline strong { font-weight: 600; }

  .steps { position: absolute; left: 15px; top: 292px; width: 534px; }
  .step {
    height: 59px; display: flex; align-items: center; color: #fff;
  }
  .step:nth-child(1) { background: var(--tint-1); }
  .step:nth-child(2) { background: var(--tint-2); }
  .step:nth-child(3) { background: var(--tint-3); }
  .step:nth-child(4) { background: var(--tint-4); }
  .step:nth-child(5) { background: var(--navy); }
  .step__label { width: 70px; text-align: right; font-size: 14px; }
  .step__number { width: 53px; text-align: center; font-size: 40px; font-weight: 300; line-height: 1; }
  .step__text { font-size: 13.5px; line-height: 17px; width: 360px; }

  .navy-field { position: absolute; left: 15px; width: 534px; background: var(--navy); }
  .page--front .navy-field { top: 587px; height: 74px; }
  .page--back .navy-field { top: 486px; height: 175px; }
  .arc { position: absolute; left: 15px; top: 598px; width: 534px; height: 64px; display: block; }

  .brand {
    position: absolute; left: 0; width: 100%; top: 690px; text-align: center; color: var(--brand-blue);
  }
  .brand__name { font-size: 31px; font-weight: 400; letter-spacing: 2px; line-height: 1; }
  .brand__tag { font-size: 8.5px; font-weight: 400; letter-spacing: 1.2px; margin-top: 4px; }
  .brand__tm {
    display: inline-block; width: 5px; height: 5px; border-radius: 50%;
    background: var(--brand-blue); vertical-align: top; margin-left: 3px;
  }

  .footer {
    position: absolute; left: 20px; right: 20px; top: 762px;
    display: flex; justify-content: space-between; color: var(--ink-blue);
    font-size: 15px; font-weight: 400;
  }
  .footer__web { letter-spacing: 2.6px; }
  .footer__phone { letter-spacing: 0.6px; }

  .model-title {
    position: absolute; left: 15px; top: 15px; width: 534px; height: 86px;
    background: var(--cyan); color: #fff; text-align: center;
  }
  .model-title h1 { font-weight: 300; font-size: 32px; margin-top: 20px; line-height: 1.1; letter-spacing: 0.3px; }
  .model-title p { font-size: 10px; }

  .model-body { position: absolute; left: 15px; top: 101px; width: 534px; height: 385px; background: var(--mid-blue); }
  .category {
    position: absolute; width: 250px; text-align: center; color: #fff;
    font-size: 11px; line-height: 13.7px;
  }
  .category h2 { font-weight: 300; font-size: 11px; }
  .category em { display: block; font-style: italic; }
  .category--exit { left: 12px; top: 11px; }
  .category--developing { left: 262px; top: 11px; }
  .category--contributing { left: 12px; top: 134px; }
  .category--emerging { left: 262px; top: 134px; }
  .category--elite { left: 142px; top: 260px; }
  .divider { position: absolute; height: 1px; background: rgba(255,255,255,0.85); width: 215px; }
  .divider--l1 { left: 29px; top: 128px; }
  .divider--r1 { left: 276px; top: 128px; }
  .divider--l2 { left: 29px; top: 248px; }
  .divider--r2 { left: 276px; top: 248px; }

  .value { position: absolute; left: 48px; top: 499px; width: 475px; color: #fff; }
  .value h3 { font-size: 12px; font-weight: 700; line-height: 15px; }
  .value p { font-size: 12px; line-height: 15px; }
</style>
</head>
<body>

<section class="page page--front">
  <div class="hero-photo" role="img" aria-label="Photo of a women's rowing crew pulling oars in unison, toned in blue"></div>
  <h2 class="headline">IS <strong>YOUR TEAM</strong> HEADING IN <strong>THE RIGHT DIRECTION?</strong></h2>
  <ol class="steps">
    <li class="step"><span class="step__label">step</span><span class="step__number">1</span><span class="step__text">Agree business critical roles and determine Talent Management priorities</span></li>
    <li class="step"><span class="step__label">step</span><span class="step__number">2</span><span class="step__text">Evaluate effectiveness of current Talent Management and succession planning processes</span></li>
    <li class="step"><span class="step__label">step</span><span class="step__number">3</span><span class="step__text">Refine talent assessment process with a focus on people in critical roles</span></li>
    <li class="step"><span class="step__label">step</span><span class="step__number">4</span><span class="step__text">Kestrel GM's organisational support assists individuals' self-assessment</span></li>
    <li class="step"><span class="step__label">step</span><span class="step__number">5</span><span class="step__text">Measure ROI and embed continual performance improvement</span></li>
  </ol>
  <div class="navy-field"></div>
  <svg class="arc" viewBox="0 0 534 64" preserveAspectRatio="none" aria-hidden="true">
    <path d="M0 64 Q267 -58 534 64 Z" fill="#ffffff"/>
  </svg>
  <div class="brand">
    <div class="brand__name">KESTREL<span class="brand__tm"></span></div>
    <div class="brand__tag">GROWTH MANAGEMENT</div>
  </div>
  <div class="footer"><span class="footer__web">www.kestrelgm.com.au</span><span class="footer__phone">Call 1800 KESTRL</span></div>
</section>

<section class="page page--back">
  <header class="model-title">
    <h1>KESTREL GROWTH MODEL</h1>
    <p>Characteristics</p>
  </header>
  <div class="model-body">
    <div class="category category--exit">
      <h2>EXIT</h2><em>planned or managed</em>
      Company or employee-initiated<br>May be disengaged/disgruntled<br>Poor hire<br>Unforeseen circumstances<br>Better opportunity<br>Conflict
    </div>
    <div class="category category--developing">
      <h2>DEVELOPING</h2><em>high risk/high reward</em>
      New talent<br>Needs to integrate external experience<br>Project-dependent<br>Growing industry connections<br>Personal brand aligned with the business
    </div>
    <div class="divider divider--l1"></div>
    <div class="divider divider--r1"></div>
    <div class="category category--contributing">
      <h2>CONTRIBUTING</h2><em>probable flight risk</em>
      Transactional<br>Track record of quantifiable results<br>Commercial<br>Stable<br>In the zone &amp; contributing today<br>Potential
    </div>
    <div class="category category--emerging">
      <h2>EMERGING</h2><em>manage career aspirations</em>
      Engaged<br>Transformational<br>Strong personal brand<br>Results multiplier who facilitates other's success<br>Promote 1 or 2 levels up
    </div>
    <div class="divider divider--l2"></div>
    <div class="divider divider--r2"></div>
    <div class="category category--elite">
      <h2>ELITE</h2><em>mission critical or market-sensitive</em>
      Executive presence<br>Established with strong external reputation<br>Potential successor to CEO<br>Mature<br>Complex issues<br>Head-hunt risk
    </div>
  </div>
  <div class="navy-field"></div>
  <div class="value">
    <h3>OUR VALUE</h3>
    <p>We assist our clients to develop and retain their elite talent through bespoke, personalised and individual coaching programs. Through this process we develop deep insight into the business and use this to assist people in other talent categories, whether they have just arrived in the business, aspire to be elite, or are leaving.</p>
  </div>
  <svg class="arc" viewBox="0 0 534 64" preserveAspectRatio="none" aria-hidden="true">
    <path d="M0 64 Q267 -58 534 64 Z" fill="#ffffff"/>
  </svg>
  <div class="brand">
    <div class="brand__name">KESTREL<span class="brand__tm"></span></div>
    <div class="brand__tag">GROWTH MANAGEMENT</div>
  </div>
  <div class="footer"><span class="footer__web">www.kestrelgm.com.au</span><span class="footer__phone">Call 1800 KESTRL</span></div>
</section>

</body>
</html>
```